Informational Site for Advanced Chemistry R&D

The company develops oxidation chemistry for air, water, fuel pollution controls. The site has been prototyped at www.velmirlab.net. Take a look. Now, the task is to design it for eye-catching beauty with use of color, on-page scroll-driven color transition and parallax effects. Should capture the themes: high technology, wow it's beautiful, modern, uncluttered, clean urban environment.

Target Market(s)

China Environmentally Conscious Government and Industry,

Industry/Entity Type

It Company

Number of Pages Required

3 page

Font styles to use
Sans Serif

Requirements
Must have
• Parallax effects, desktop compatible, Rich, Modern, Simple, Graphic
Nice to have
• Mobile Phone Compatible
Should not have
• Flash, or anything that is slow to load or requires high bandwidth

```html
<!DOCTYPE html>
<html lang="en">
<head>
<meta charset="utf-8">
<title>Velmir Lab — Advanced Oxidation Science</title>
<link href="https://fonts.googleapis.com/css2?family=Open+Sans:wght@400;600;700;800&family=Oswald:wght@500;600&display=swap" rel="stylesheet">
<style>
:root{
  --blue:#1b68b3;
  --blue-dark:#145494;
  --blue-mid:#2f7fc8;
  --blue-light:#4f8fcf;
  --teal:#2bb3a6;
  --teal-dark:#21978c;
  --ink:#222;
  --text:#555;
  --night-2:#2a2c2e;
  --paper:#fff;
}
*{box-sizing:border-box;margin:0;padding:0}
html,body{width:1200px;height:3163px;overflow:hidden}
body{position:relative;background:var(--paper);font-family:"Open Sans",Arial,sans-serif;color:var(--text)}
.abs{position:absolute}

/* Hero */
.hero-bg{left:0;top:0;width:1200px;height:574px;background:linear-gradient(180deg,#2c3a44 0%,#4b5b63 35%,#5e6a66 60%,#2f3a30 82%,#1c241c 100%)}
.topbar{left:0;top:0;width:1200px;height:25px;background:rgba(0,0,0,.35);font-size:10px;color:#dfe6ea}
.topbar .mail{left:260px;top:6px}
.topbar .tel{left:378px;top:6px}
.topbar .dot{display:inline-block;width:9px;height:7px;background:var(--teal);margin-right:5px;vertical-align:-1px}
.topbar .soc{top:7px;width:11px;height:11px;background:rgba(255,255,255,.45)}
.logo{left:270px;top:68px;display:flex;align-items:center;gap:8px;color:#fff;font-weight:700;font-size:16px}
.logo i{display:block;width:20px;height:20px;border-radius:50%;background:var(--blue-mid)}
.nav{left:374px;top:50px;display:flex;gap:16px;font-size:10px;font-weight:600;color:#fff;letter-spacing:.2px}
.contact-btn{left:854px;top:38px;width:76px;height:31px;border:2px solid var(--teal);color:#fff;font-size:9px;font-weight:700;display:flex;align-items:center;justify-content:center;background:rgba(0,0,0,.25)}
.hero-title{left:0;width:1200px;top:218px;text-align:center;color:#fff;font-weight:700;font-size:50px;line-height:60px;letter-spacing:.5px}
.hero-sub{left:0;width:1200px;top:274px;text-align:center;color:#fff;font-weight:700;font-size:23px;line-height:30px}
.btn-teal{background:var(--teal);color:#fff;font-weight:600;display:flex;align-items:center;justify-content:center}
.hero-cta{left:506px;top:327px;width:188px;height:42px;font-size:13px}

/* Welcome */
.welcome-title{left:0;width:1200px;top:624px;text-align:center;color:var(--blue);font-weight:800;font-size:40px;line-height:48px}
.welcome-sub{left:0;width:1200px;top:668px;text-align:center;color:var(--ink);font-size:18px}
.welcome-copy{left:264px;width:674px;top:706px;text-align:center;font-size:10.5px;line-height:15px}
.tabs{left:249px;top:776px;width:700px;height:152px;display:flex}
.tab{flex:1;color:#fff;text-align:center;padding:38px 18px 0;font-size:9.5px;line-height:13px}
.tab b{display:block;font-size:9px;letter-spacing:.6px;margin-bottom:20px}
.tab.history{background:var(--blue-dark)}
.tab.vision{background:var(--teal)}
.tab.mission{background:var(--blue-mid)}
.tab.values{background:var(--blue-light)}
.tab .more{display:inline-block;margin-top:16px;background:var(--blue-dark);padding:5px 14px;font-weight:700;font-size:9px}
.tab-strip{left:249px;top:928px;width:700px;height:7px;background:var(--teal)}

/* Service grid */
.photo{height:325px}
.coal{left:0;top:998px;width:600px;background:linear-gradient(135deg,#3d3a35 0%,#6a5a44 40%,#b89a3a 70%,#3a3630 100%)}
.water{left:600px;top:998px;width:600px;background:linear-gradient(180deg,#5aa7df 0%,#9cc9ea 45%,#4f8aa6 70%,#2f5f70 100%)}
.diesel{left:0;top:1323px;width:600px;background:linear-gradient(180deg,#3a2410 0%,#b35a14 45%,#f2a42a 65%,#6b3210 100%)}
.soil{left:600px;top:1323px;width:600px;background:linear-gradient(135deg,#9aa0a6 0%,#6c7c46 40%,#5a8a2e 65%,#a0522d 100%)}
.card-frame{width:238px;height:310px;background:var(--blue);padding:10px}
.card{position:relative;width:100%;height:100%;background:#fff;padding:20px 16px 0;overflow:hidden}
.card::after{content:"";position:absolute;right:0;top:0;border-top:16px solid var(--blue);border-left:16px solid transparent}
.card h3{font-size:17px;font-weight:700;color:var(--ink);white-space:nowrap}
.card .bar{width:100%;height:1px;background:#ddd;margin:10px 0 12px}
.card p{font-size:9.5px;line-height:13.5px;margin-bottom:10px}
.card p a{color:var(--teal-dark);text-decoration:underline}
.card .learn{position:absolute;right:16px;bottom:12px;font-size:9px;font-weight:700;color:var(--blue)}

/* Band */
.band{left:0;top:1645px;width:1200px;height:133px;background:var(--night-2)}
.band h4{left:170px;width:500px;top:42px;text-align:right;font-family:"Oswald",Arial,sans-serif;font-weight:500;font-size:22px;line-height:28px;color:#fff}
.band .tag{left:170px;width:500px;top:74px;text-align:right;font-size:12px;color:#fff}
.band .tag b{font-weight:700}
.band .advice{left:734px;top:32px;width:177px;height:28px;background:#fff;color:var(--ink);font-size:10px;font-weight:700;display:flex;align-items:center;justify-content:center}
.band .phone{left:734px;top:72px;display:flex;align-items:center;gap:8px;color:#fff;font-size:19px;font-weight:700}

/* Testimonials */
.testi{left:0;top:1778px;width:1200px;height:536px;background:radial-gradient(ellipse at 50% 40%,#fafafa 0%,#e9eaeb 70%,#dcdedf 100%)}
.testi h2{left:0;width:1200px;top:52px;text-align:center;color:var(--blue);font-weight:800;font-size:40px;line-height:48px}
.testi .sub{left:0;width:1200px;top:96px;text-align:center;color:var(--ink);font-size:18px}
.person{top:136px;width:220px;text-align:center}
.avatar{width:130px;height:130px;margin:0 auto;border-radius:50%;border:5px solid #fff;box-shadow:0 2px 6px rgba(0,0,0,.2);background:linear-gradient(180deg,#c9ccd0,#8d959c)}
.person .name{margin-top:22px;color:var(--blue);font-weight:700;font-size:10.5px}
.person .role{font-size:9px;font-style:italic;color:var(--ink);font-weight:600}
.person p{margin-top:8px;font-size:10px;line-height:14px}
.dots{left:584px;top:466px;display:flex;gap:6px}
.dots i{width:5px;height:5px;border-radius:50%;background:#9ab}
.dots i.on{background:var(--blue)}

/* Contact */
.contact{left:0;top:2314px;width:1200px;height:614px;background:linear-gradient(180deg,#1c1d1f,#262729)}
.field{background:#fff;font-size:8px;color:#666;padding:8px 10px;font-weight:600}
.captcha{left:491px;top:210px;width:104px;height:30px;border:1px solid #777;background:#eee;color:#333;font-size:12px;font-style:italic;display:flex;align-items:center;justify-content:center;font-weight:700}
.captcha-in{left:605px;top:210px;width:104px;height:30px;border:1px solid #777;color:#ccc;font-size:9px;display:flex;align-items:center;justify-content:center}
.submit{left:447px;top:272px;width:304px;height:33px;font-size:12px}
.contact h2{left:0;width:1200px;top:356px;text-align:center;color:#fff;font-weight:700;font-size:36px;line-height:44px}
.contact .stay{left:0;width:1200px;top:402px;text-align:center;color:#fff;font-size:18px}
.socials{left:498px;top:447px;display:flex;gap:5px}
.socials span{width:38px;height:38px;border-radius:50%;background:var(--blue-mid);color:#fff;font-size:10px;font-weight:700;display:flex;align-items:center;justify-content:center}

/* Footer */
.footer{left:0;top:2928px;width:1200px;height:50px;background:#141516;font-size:8px;color:#ccc}
.footer .copy{left:256px;top:12px;line-height:12px}
.sea{left:0;top:2978px;width:1200px;height:185px;background:linear-gradient(180deg,#1a6f78 0%,#27a5a5 45%,#0f4f5a 100%)}
.seal{left:494px;top:2858px;width:210px;height:210px;border-radius:50%;background:#fff;border:10px solid #1a1a1a;display:flex;align-items:center;justify-content:center;flex-direction:column;gap:8px;color:var(--blue);font-weight:700;font-size:22px}
.seal i{display:block;width:34px;height:34px;border-radius:50%;background:var(--teal)}
</style>
</head>
<body>

<div class="abs hero-bg" role="img" aria-label="Storm clouds and a tornado over a green river valley"></div>
<div class="abs topbar">
  <span class="abs mail"><span class="dot"></span>support@velmirlab.net</span>
  <span class="abs tel"><span class="dot"></span>+1.555.210.487</span>
  <span class="abs soc" style="left:849px"></span>
  <span class="abs soc" style="left:865px"></span>
  <span class="abs soc" style="left:881px"></span>
  <span class="abs soc" style="left:897px"></span>
  <span class="abs soc" style="left:913px"></span>
</div>
<div class="abs logo"><i></i>Velmir Lab</div>
<nav class="abs nav"><span>HOME</span><span>ABOUT US</span><span>COAL FLUE GAS</span><span>WASTEWATER</span><span>DIESEL FUEL</span><span>VOLATILE ORGANICS</span></nav>
<div class="abs contact-btn">CONTACT US</div>
<h1 class="abs hero-title">ADVANCED OXIDATION</h1>
<p class="abs hero-sub">SCIENCE FOR ENVIRONMENTAL POLLUTION MANAGEMENT</p>
<div class="abs btn-teal hero-cta">GET FREE EXPERT ADVICE</div>

<h2 class="abs welcome-title">WELCOME</h2>
<p class="abs welcome-sub">TO THE VELMIR LAB CORPORATION</p>
<p class="abs welcome-copy">Lorem ipsum dolor sit amet, consectetur adipiscing elit, sed do eiusmod tempor incididunt ut labore et dolore magna aliqua. Ut enim ad minim veniam, quis nostrud exercitation ullamco laboris nisi ut aliquip ex ea commodo consequat. Duis aute irure dolor in reprehenderit in voluptate velit esse cillum dolore eu fugiat nulla pariatur. Excepteur sint occaecat cupidatat non proident.</p>
<div class="abs tabs">
  <div class="tab history"><b>HISTORY</b>Claritas est etiam processus dynamicus, qui sequitur mutationem consuetudium lectorum.</div>
  <div class="tab vision"><b>VISION</b>Claritas est etiam processus dynamicus, qui sequitur mutationem consuetudium lectorum.<br><span class="more">MORE</span></div>
  <div class="tab mission"><b>MISSION</b>Claritas est etiam processus dynamicus, qui sequitur mutationem consuetudium lectorum.</div>
  <div class="tab values"><b>VALUES</b>Claritas est etiam processus dynamicus, qui sequitur mutationem consuetudium lectorum.</div>
</div>
<div class="abs tab-strip"></div>

<div class="abs photo coal" role="img" aria-label="Open-pit coal mine with excavator and yellow haul truck"></div>
<div class="abs photo water" role="img" aria-label="Wastewater treatment basin under blue sky"></div>
<div class="abs photo diesel" role="img" aria-label="Oil pump jack silhouetted against an orange sunset"></div>
<div class="abs photo soil" role="img" aria-label="Worker in gloves sampling red soil among green plants"></div>

<article class="abs card-frame" style="left:360px;top:1006px">
  <div class="card"><h3>COAL FLUE GAS</h3><div class="bar"></div>
  <p>Lorem ipsum dolor sit amet, consectetur adipiscing elit, sed do eiusmod tempor incididunt ut labore et dolore magna aliqua. Ut enim ad minim veniam, quis nostrud <a>exercitation ullamco laboris nisi ut aliquip ex</a> ea commodo consequat.</p>
  <p>Duis aute irure dolor in reprehenderit in voluptate velit esse cillum dolore eu fugiat nulla pariatur. Excepteur sint occaecat cupidatat non proident.</p>
  <span class="learn">LEARN MORE ›</span></div>
</article>
<article class="abs card-frame" style="left:962px;top:1006px">
  <div class="card"><h3>WASTEWATER</h3><div class="bar"></div>
  <p>Lorem ipsum dolor sit amet, consectetur adipiscing elit, sed do eiusmod tempor incididunt ut labore et dolore magna aliqua. Ut enim ad minim veniam, quis nostrud <a>exercitation ullamco laboris nisi ut aliquip ex</a> ea commodo consequat.</p>
  <p>Duis aute irure dolor in reprehenderit in voluptate velit esse cillum dolore eu fugiat nulla pariatur. Excepteur sint occaecat cupidatat non proident.</p>
  <span class="learn">LEARN MORE ›</span></div>
</article>
<article class="abs card-frame" style="left:0;top:1330px">
  <div class="card"><h3>DIESEL FUEL</h3><div class="bar"></div>
  <p>Lorem ipsum dolor sit amet, consectetur adipiscing elit, sed do eiusmod tempor incididunt ut labore et dolore magna aliqua. Ut enim ad minim veniam, quis nostrud <a>exercitation ullamco laboris nisi ut aliquip ex</a> ea commodo consequat.</p>
  <p>Duis aute irure dolor in reprehenderit in voluptate velit esse cillum dolore eu fugiat nulla pariatur. Excepteur sint occaecat cupidatat non proident.</p>
  <span class="learn">LEARN MORE ›</span></div>
</article>
<article class="abs card-frame" style="left:601px;top:1330px">
  <div class="card"><h3>VOLATILE ORGANICS</h3><div class="bar"></div>
  <p>Lorem ipsum dolor sit amet, consectetur adipiscing elit, sed do eiusmod tempor incididunt ut labore et dolore magna aliqua. Ut enim ad minim veniam, quis nostrud <a>exercitation ullamco laboris nisi ut aliquip ex</a> ea commodo consequat.</p>
  <p>Duis aute irure dolor in reprehenderit in voluptate velit esse cillum dolore eu fugiat nulla pariatur. Excepteur sint occaecat cupidatat non proident.</p>
  <span class="learn">LEARN MORE ›</span></div>
</article>

<section class="abs band">
  <h4 class="abs">ENVIRONMENTAL POLLUTION CONTROL SOLUTIONS</h4>
  <p class="abs tag">employing nature's most reactive <b>Free Radical</b></p>
  <div class="abs advice">GET FREE EXPERT ADVICE</div>
  <div class="abs phone">
    <svg width="22" height="22" viewBox="0 0 24 24" aria-hidden="true"><path fill="#fff" d="M6.6 10.8a15.2 15.2 0 0 0 6.6 6.6l2.2-2.2c.3-.3.7-.4 1-.2 1.1.4 2.3.6 3.6.6.6 0 1 .4 1 1V20c0 .6-.4 1-1 1A17 17 0 0 1 3 4c0-.6.4-1 1-1h3.5c.6 0 1 .4 1 1 0 1.3.2 2.5.6 3.6.1.3 0 .7-.2 1z"/></svg>
    +1.555.210.487
  </div>
</section>

<section class="abs testi">
  <h2 class="abs">TESTIMONIALS</h2>
  <p class="abs sub">CLIENTS SAYS ABOUT VELMIR LAB</p>
  <div class="abs person" style="left:257px">
    <div class="avatar" role="img" aria-label="Portrait of client Owen Harlow"></div>
    <div class="name">OWEN HARLOW</div><div class="role">Manager, Northgate Works</div>
    <p>Reprehenderit in voluptate velit esse cillum dolore eu fugiat nulla pariatur. Excepteur sint occaecat cupidatat non proident, sunt in culpa qui officia deserunt mollit anim id est laborum. Sed ut perspiciatis unde omnis iste natus error sit voluptatem accusantium doloremque laudantium, totam rem aperiam eaque ipsa.</p>
  </div>
  <div class="abs person" style="left:490px">
    <div class="avatar" role="img" aria-label="Portrait of client Lena Marsh"></div>
    <div class="name">LENA MARSH</div><div class="role">Manager, Northgate Works</div>
    <p>Reprehenderit in voluptate velit esse cillum dolore eu fugiat nulla pariatur. Excepteur sint occaecat cupidatat non proident, sunt in culpa qui officia deserunt mollit anim id est laborum. Sed ut perspiciatis unde omnis iste natus error sit voluptatem accusantium doloremque laudantium, totam rem aperiam eaque ipsa.</p>
  </div>
  <div class="abs person" style="left:723px">
    <div class="avatar" role="img" aria-label="Portrait of client Tomas Reed"></div>
    <div class="name">TOMAS REED</div><div class="role">Manager, Northgate Works</div>
    <p>Reprehenderit in voluptate velit esse cillum dolore eu fugiat nulla pariatur. Excepteur sint occaecat cupidatat non proident, sunt in culpa qui officia deserunt mollit anim id est laborum. Sed ut perspiciatis unde omnis iste natus error sit voluptatem accusantium doloremque laudantium, totam rem aperiam eaque ipsa.</p>
  </div>
  <div class="abs dots"><i></i><i class="on"></i><i></i></div>
</section>

<section class="abs contact">
  <div class="abs field" style="left:316px;top:59px;width:277px;height:27px">NAME</div>
  <div class="abs field" style="left:605px;top:59px;width:277px;height:27px">EMAIL</div>
  <div class="abs field" style="left:316px;top:99px;width:566px;height:82px">MESSAGE</div>
  <div class="abs captcha">Xq7rTa</div>
  <div class="abs captcha-in">Enter captcha</div>
  <div class="abs btn-teal submit">SUBMIT YOUR MESSAGE</div>
  <h2 class="abs">CONNECT US</h2>
  <p class="abs stay">YOU SHOULD STAY IN TOUCH!</p>
  <div class="abs socials"><span>TW</span><span>YT</span><span>FB</span><span>GP</span><span>IN</span></div>
</section>

<footer class="abs footer">
  <p class="abs copy">© 2016, Velmir Lab Corporation. All Rights Reserved.<br>Use of T&amp;C &nbsp;|&nbsp; Sitemap</p>
</footer>
<div class="abs sea" role="img" aria-label="Aerial view of turquoise ocean waves"></div>
<div class="abs seal"><i></i>Velmir Lab</div>

</body>
</html>
```